Company Letter head for real estate company

need company letter head
Updates

You can use the logo that I submitted. no need to create a new one

Requirements
Must have
• must have my address on it..38264 WINDMERE, CANTON, MI 48302-1175, INFO@MUVRO.CA

```html
<!DOCTYPE html>
<html lang="en">
<head>
<meta charset="utf-8">
<title>Muvro Letterhead</title>
<link href="https://fonts.googleapis.com/css2?family=Open+Sans:ital,wght@0,400;0,600;0,700;1,400&family=PT+Serif:wght@700&display=swap" rel="stylesheet">
<style>
  :root {
    --green: #5ca32e;
    --green-dark: #2f6b1f;
    --green-light: #9fd25a;
    --ink: #1e1e1e;
    --ink-soft: #4a4a4a;
    --paper: #ffffff;
  }
  * { box-sizing: border-box; margin: 0; padding: 0; }
  html, body { width: 900px; height: 1200px; overflow: hidden; background: var(--paper); }
  body { font-family: "Open Sans", Arial, sans-serif; color: var(--ink); }
  .letterhead { position: relative; width: 900px; height: 1200px; overflow: hidden; }

  .brand { position: absolute; left: 80px; top: 90px; display: flex; align-items: center; gap: 14px; }
  .brand-dot { width: 30px; height: 30px; border-radius: 50%; background: var(--green); }
  .brand-name { font-weight: 700; font-size: 52px; letter-spacing: 2px; color: var(--green-dark); }

  .contact { position: absolute; left: 520px; top: 70px; list-style: none; }
  .contact li { display: flex; align-items: center; gap: 12px; height: 40px; font-size: 19px; color: var(--ink-soft); }
  .contact svg { width: 26px; height: 26px; flex: none; }

  .recipient { position: absolute; left: 80px; top: 250px; }
  .recipient h2 { font-size: 22px; font-weight: 700; line-height: 1.3; }
  .recipient address { margin-top: 14px; font-size: 15px; font-style: italic; line-height: 1.35; color: var(--ink-soft); }

  .salutation { position: absolute; left: 80px; top: 430px; font-family: "PT Serif", Georgia, serif; font-size: 44px; font-weight: 700; }

  .body-copy { position: absolute; left: 80px; top: 505px; width: 740px; }
  .body-copy p { font-size: 13.5px; line-height: 1.55; color: var(--ink-soft); margin-bottom: 16px; text-align: justify; }

  .sign-off { position: absolute; right: 80px; top: 870px; text-align: right; font-size: 13px; line-height: 1.4; color: var(--ink-soft); }
  .sign-off strong { color: var(--ink); font-weight: 600; }
  .signature { display: block; margin: 8px 0 0 auto; width: 110px; height: 44px; background: #e8e8e8; border-radius: 4px; }

  .landscape { position: absolute; left: 0; bottom: 0; width: 900px; height: 260px; }
</style>
</head>
<body>
<main class="letterhead">

  <header>
    <div class="brand">
      <span class="brand-dot"></span>
      <span class="brand-name">MUVRO</span>
    </div>
    <ul class="contact">
      <li>
        <svg viewBox="0 0 26 26"><rect width="26" height="26" rx="5" fill="var(--green)"/><path d="M9 6l3 3-2 2a10 10 0 0 0 5 5l2-2 3 3-2 3c-6 0-12-6-12-12z" fill="#fff"/></svg>
        48302-1175
      </li>
      <li>
        <svg viewBox="0 0 26 26"><rect width="26" height="26" rx="5" fill="var(--green)"/><path d="M13 5a5 5 0 0 0-5 5c0 4 5 11 5 11s5-7 5-11a5 5 0 0 0-5-5zm0 7a2 2 0 1 1 0-4 2 2 0 0 1 0 4z" fill="#fff"/></svg>
        38264 windmere, canton
      </li>
      <li>
        <svg viewBox="0 0 26 26"><rect width="26" height="26" rx="5" fill="var(--green)"/><rect x="6" y="8" width="14" height="10" rx="1" fill="#fff"/><path d="M6 8l7 6 7-6" stroke="var(--green)" stroke-width="1.5" fill="none"/></svg>
        info@muvro.ca
      </li>
      <li>
        <svg viewBox="0 0 26 26"><rect width="26" height="26" rx="5" fill="var(--green)"/><circle cx="13" cy="13" r="7" fill="none" stroke="#fff" stroke-width="1.6"/><path d="M6 13h14M13 6c-3 4-3 10 0 14M13 6c3 4 3 10 0 14" stroke="#fff" stroke-width="1.4" fill="none"/></svg>
        www.muvro.ca
      </li>
    </ul>
  </header>

  <section class="recipient">
    <h2>To: Sir, Alan Reyes<br>CEO of Brightline Group</h2>
    <address>Harbor Lane 48<br>Riverton, CA 90410<br>USA</address>
  </section>

  <h1 class="salutation">Dear Sir,</h1>

  <section class="body-copy">
    <p>We are pleased to introduce our residential and commercial property services across the Canton region. Our team of licensed agents has supported buyers, sellers and investors for many years, guiding each client from the first viewing through to the final signature. We believe every property decision deserves careful research, honest advice and clear communication, and we would welcome the opportunity to discuss how we can support the goals of your organisation in the coming year.</p>
    <p>Our portfolio includes family homes, modern condominiums, retail units and office space, each selected for location, value and long-term potential. We provide market reports, property valuations and tailored search plans, and our leasing team manages contracts, inspections and tenant relations on behalf of owners. With local knowledge and a wide network of partners, we can match your requirements with suitable listings quickly and with full transparency at every stage.</p>
    <p>Please find our current brochure enclosed with this letter. We would be glad to arrange a meeting at a time that suits you, either at our office or at your premises.</p>
  </section>

  <div class="sign-off">
    Yours sincerely,<br>
    <strong>Evan Marsh Holloway</strong>
    <span class="signature" role="img" aria-label="Handwritten signature"></span>
  </div>

  <svg class="landscape" viewBox="0 0 900 260" preserveAspectRatio="none" role="img" aria-label="Green rolling hills with clusters of pine trees at left and right">
    <defs>
      <linearGradient id="hillTone" x1="0" y1="0" x2="0" y2="1">
        <stop offset="0" stop-color="var(--green-light)"/>
        <stop offset="1" stop-color="var(--green-dark)"/>
      </linearGradient>
    </defs>
    <path d="M0 40 L0 260 L900 260 L900 50 C760 140 600 190 450 190 C300 190 140 150 0 40 Z" fill="url(#hillTone)"/>
  </svg>

</main>
</body>
</html>
```